Counsel Atelier

we need all the matirials for the office to speak with the internet site
www.corvenfirm-example.com

look stilish and modern yet very respecteble

our logo needs to be our logo and some times

just the letters " Corven " done nicely.

We need to send e mails with a design

Firm paper

and our gmail products to look nice when we use google docs

so we need a place for

lawers names and

the corven

and logo

and address

and some one to help us do it all

Target Market(s)

Big firms

Industry/Entity Type

Law Firm

Font styles to use
Serif

Requirements
Must have
• Rememrable
• Different yet respectable
• For multi languages
• LAW
• B
• LAWYERS
• BOUTIQUE
Nice to have
• Clean Design
• impressive
• i put on a new card i liked
• We should not put any decorations and beautiful logo
• it's against the law for lawyers
• I have a card that proves that we are smart and boutiques
• This card that I attached as an example
• Makes you little work, and certainly - apart from everyone
• Would love this design idea
• The numbers stated hiding it from top to bottom
• I put my real information integration profile
• The thing is that people should enlighten other options and other card
• This should be accessible designer fee changes
• Still very respectable and serious
• it needs to say among other creative stuff
• Counsel atelier CORVEN
• MARCUS TELLION
• 052-7196205
• 1@corvenfirm-example.com
• www.corvenfirm-example.com
• but any smart idea
Should not have
• We have a problam
• It turns out that the law of the Bar Association in
• Our country
• Do not allow to put the firm logo on business cards
• Or office paper
• the logo can only be letters and names
• So we should convey the idea of all sorts of areas along
• As we tried with our logo
• Through the letters themselves
• And their integration with each other

```html
<!DOCTYPE html>
<html lang="en">
<head>
<meta charset="utf-8">
<title>Corven — Business Card</title>
<link rel="stylesheet" href="https://fonts.googleapis.com/css2?family=Questrial&family=Montserrat:wght@500;600&display=swap">
<style>
  :root {
    --page: #2a2a2c;
    --navy: #0d2a6e;
    --navy-deep: #0a2060;
    --navy-light: #1f3f8c;
    --paper: #ffffff;
    --ink-light: #ffffff;
    --ink-soft: #c9d3ea;
  }
  * { box-sizing: border-box; margin: 0; padding: 0; }
  html, body {
    width: 1200px; height: 843px; overflow: hidden;
    background: var(--page);
  }
  .sheet {
    width: 1200px; height: 843px;
    display: flex; flex-direction: column;
    align-items: center; justify-content: center; gap: 40px;
  }
  .card {
    width: 630px; height: 360px;
    position: relative; overflow: hidden;
    box-shadow: 0 10px 30px rgba(0,0,0,.45);
    font-family: "Questrial", "Century Gothic", sans-serif;
  }
  .band-navy {
    background: linear-gradient(100deg, var(--navy-deep) 0%, var(--navy) 35%, var(--navy-light) 55%, var(--navy) 75%, var(--navy-deep) 100%);
  }

  /* Back face */
  .card-back {
    display: flex; flex-direction: column; align-items: center; justify-content: center;
  }
  .card-back .wordmark {
    color: var(--ink-light);
    font-size: 78px; letter-spacing: 10px;
  }
  .card-back .site {
    margin-top: 14px;
    color: var(--ink-soft);
    font-size: 13px; letter-spacing: 6px;
  }

  /* Front face */
  .card-front .top {
    position: absolute; inset: 0 0 auto 0; height: 158px;
    background: var(--paper);
    display: flex; align-items: center; justify-content: center;
  }
  .card-front .wordmark {
    color: var(--navy);
    font-size: 78px; letter-spacing: 10px;
    padding-top: 8px;
  }
  .card-front .bottom {
    position: absolute; inset: 158px 0 0 0;
  }
  .holder {
    position: absolute; left: 34px; top: 22px;
    color: var(--ink-light);
  }
  .holder .name {
    font-family: "Montserrat", "Helvetica", sans-serif;
    font-weight: 600; font-size: 19px;
  }
  .holder .role {
    margin-top: 3px; font-size: 14px; color: var(--ink-soft);
  }
  .contact {
    position: absolute; right: 34px; top: 50px; width: 240px;
    color: var(--ink-light); font-size: 14px; line-height: 1.4;
  }
  .contact .address { margin-bottom: 12px; }
  .contact ul { list-style: none; }
  .contact li { display: flex; align-items: center; gap: 12px; margin-bottom: 4px; }
  .contact svg { width: 14px; height: 14px; flex: none; }
</style>
</head>
<body>
<main class="sheet">
  <section class="card card-back band-navy" aria-label="Card back">
    <div class="wordmark">Corven</div>
    <div class="site">www.corvenfirm-example.com</div>
  </section>

  <section class="card card-front" aria-label="Card front">
    <div class="top">
      <div class="wordmark">Corven</div>
    </div>
    <div class="bottom band-navy">
      <div class="holder">
        <div class="name">Marcus Tellion</div>
        <div class="role">Attorney</div>
      </div>
      <div class="contact">
        <div class="address">4127 Harrowgate Lane<br>Brookhaven, NY 11719</div>
        <ul>
          <li>
            <svg viewBox="0 0 16 16" aria-hidden="true"><path fill="#fff" d="M3.5 1.5l2.5 2.5-1.5 2a9 9 0 0 0 5.5 5.5l2-1.5 2.5 2.5-2 2C6 14 2 10 1.5 3.5z"/></svg>
            <span>052-7196205</span>
          </li>
          <li>
            <svg viewBox="0 0 16 16" aria-hidden="true"><rect x="1" y="3" width="14" height="10" fill="#fff"/><path d="M1 3l7 6 7-6" fill="none" stroke="#0d2a6e" stroke-width="1.4"/></svg>
            <span>1@corvenfirm-example.com</span>
          </li>
          <li>
            <svg viewBox="0 0 16 16" aria-hidden="true"><circle cx="8" cy="8" r="6.5" fill="#fff"/><path d="M1.5 8h13M8 1.5c-3 3.5-3 9.5 0 13M8 1.5c3 3.5 3 9.5 0 13" fill="none" stroke="#0d2a6e" stroke-width="1"/></svg>
            <span>www.corvenfirm-example.com</span>
          </li>
        </ul>
      </div>
    </div>
  </section>
</main>
</body>
</html>
```